Camp Maplebrook Summer Programs Postcard

We need a postcard design for summer 2017 programs. Camp Maplebrook offers nine weeks of day camp and one week of overnight camp. We are a Christian summer camp. We offer lots of activities like swimming, archery, rock wall, zipline, sports, crafts, drama and more. We want to showcase the activities we offer. The design should communicate outdoor fun and friendship. We want to focus on high quality photos that reflect the activities we offer.

Target Market(s)

Elementary age children/parents

Industry/Entity Type

Childcare

Font styles to use
Serif

Requirements
Must have
• Camp Maplebrook "Christian Camping Since 1952"
• Day Camp 2017 "Courageous Campers"
• June 19 - August 18
• $130 per week
• Mon-Fri 8 am to 4 pm. Open to all kids entering grades 1 to 8. Day camp is chock full of activities like swimming, rock wall, archery, zipline, sports, campfires and much more! Daily lunch and snack included. Before and after-care available at an extra rate.
• Overnight Camp 2017
• July 16 - 22
• $325
• Open to all kids ages 8 to 14. Spend the week making new friends, sleeping in cabins, climbing the rock wall and ziplining under the stars! Our special guest speaker will lead twice daily chapel sessions that will challenge campers to grow in their faith.
• Register and pay for 7 weeks by May 1st, get 2 FREE!
• Website: www.maplebrook-example.org
• Address: 41 Cedar Vale Rd. Lisford, NH 03999
• Phone: 603-555-0148

```html
<!DOCTYPE html>
<html lang="en">
<head>
<meta charset="utf-8">
<title>Camp Maplebrook Summer Programs Postcard</title>
<link rel="stylesheet" href="https://fonts.googleapis.com/css2?family=Montserrat:ital,wght@0,400;0,500;0,600;0,700;1,500&family=Roboto+Slab:wght@700;800&display=swap">
<style>
  :root{
    --bg:#e6e6e6;
    --orange:#d0482c;
    --red:#c41f30;
    --title-red:#cf3a26;
    --ink:#3a3a3a;
    --muted:#555;
    --white:#fff;
    --photo-green:#7a9a5c;
    --photo-warm:#c98a6a;
    --photo-sky:#9fb3b8;
  }
  *{box-sizing:border-box;margin:0;padding:0}
  html,body{width:1200px;height:1200px;overflow:hidden}
  body{background:var(--bg);font-family:"Montserrat",sans-serif;color:var(--ink);position:relative}

  .card{position:absolute;left:230px;width:741px;height:530px;overflow:hidden}
  .card--front{top:54px;background:var(--orange)}
  .card--back{top:614px;background:var(--white)}

  .panel{position:absolute;left:44px;top:20px;width:666px;height:480px}

  .tagline{position:absolute;left:96px;top:19px;width:263px;height:60px;background:var(--red);
    transform:rotate(-1.5deg);border-radius:3px 3px 5px 5px;color:var(--white);
    font-family:"Roboto Slab",serif;font-weight:800;font-size:19px;line-height:22px;
    text-align:center;padding-top:8px}

  .photo{position:absolute;border:4px solid var(--white);border-radius:12px;
    box-shadow:0 2px 5px rgba(0,0,0,.25)}
  .photo--climb{left:34px;top:70px;width:184px;height:180px;transform:rotate(3deg);
    background:linear-gradient(135deg,var(--photo-green),#4f6a3c)}
  .photo--friends{left:214px;top:110px;width:144px;height:144px;transform:rotate(3deg);
    background:linear-gradient(135deg,#6a6a7a,var(--photo-warm))}
  .photo--smile{left:42px;top:250px;width:152px;height:148px;transform:rotate(4deg);
    background:linear-gradient(135deg,#d9c9b4,var(--photo-warm))}
  .photo--wall{left:197px;top:254px;width:146px;height:144px;transform:rotate(3deg);
    background:linear-gradient(135deg,var(--photo-sky),var(--photo-green))}

  .brand{position:absolute;display:flex;align-items:center;gap:10px;
    font-weight:700;color:var(--red);line-height:1.05}
  .brand__dot{width:20px;height:20px;border-radius:50%;background:var(--red);flex:none}
  .brand__name span{display:block}
  .card--front .brand{left:436px;top:82px;font-size:32px}
  .card--back .brand{left:66px;top:46px;font-size:32px}

  .programs{position:absolute;left:386px;top:164px;width:300px}
  .program__head{padding:3px 0 3px 32px;margin-left:-30px;background:linear-gradient(90deg,rgba(240,220,218,.9),rgba(255,255,255,0))}
  .program__title{color:var(--title-red);font-weight:600;font-size:13.5px}
  .program__dates{font-style:italic;font-weight:500;font-size:12px;color:#333}
  .program__body{font-size:9px;line-height:12.3px;color:var(--muted);margin-top:7px}
  .program__body b{color:#222;font-weight:700}
  .program__price{color:var(--red);font-weight:700;font-size:13px;margin-top:5px}
  .program + .program{margin-top:8px}

  .promo{position:absolute;left:92px;top:406px;width:270px;text-align:center;color:var(--red);
    transform:rotate(2.5deg);font-weight:600;font-size:12.5px}
  .promo strong{display:block;font-size:20px;font-weight:700;color:var(--title-red)}

  .phone{position:absolute;left:374px;top:434px;width:262px;height:62px;background:var(--red);
    transform:rotate(2deg);border-radius:5px;color:var(--white);font-weight:700;font-size:26px;
    text-align:center;line-height:62px}

  .footer{position:absolute;left:24px;top:497px;font-size:11.5px;color:var(--white)}
  .footer b{font-weight:700;margin-left:16px}
  .footer b:first-child{margin-left:0}

  .back__label{position:absolute;left:66px;top:144px;font-size:13px;font-weight:700;color:var(--title-red)}
  .back__address{position:absolute;left:66px;top:162px;font-size:13.5px;color:var(--muted)}
  .back__divider{position:absolute;left:370px;top:28px;width:1px;height:462px;background:#777}
  .back__stamp{position:absolute;left:613px;top:28px;width:97px;height:128px;border:1px solid #777}
</style>
</head>
<body>

<section class="card card--front">
  <svg class="panel" viewBox="0 0 666 480" aria-hidden="true">
    <path d="M40 6 L620 0 Q660 0 662 40 L650 440 Q648 478 610 478 L36 470 Q4 468 4 430 L8 46 Q8 8 40 6Z" fill="#fff"/>
    <path d="M46 14 L614 10 Q650 10 650 46 L640 432 Q638 466 606 466 L42 460 Q14 458 14 428 L18 50 Q18 16 46 14Z" fill="none" stroke="#d0482c" stroke-width="1" stroke-dasharray="6 5"/>
  </svg>

  <div class="tagline">Christian Camping<br>Since 1952</div>

  <div class="photo photo--climb" role="img" aria-label="Photo of a camper climbing a rope course among trees"></div>
  <div class="photo photo--friends" role="img" aria-label="Photo of two girls smiling together at camp"></div>
  <div class="photo photo--smile" role="img" aria-label="Photo of a smiling young camper"></div>
  <div class="photo photo--wall" role="img" aria-label="Photo of a child climbing the rock wall"></div>

  <div class="brand"><span class="brand__dot"></span><div class="brand__name"><span>Camp</span><span>Maplebrook</span></div></div>

  <div class="programs">
    <div class="program">
      <div class="program__head">
        <div class="program__title">Day Camp 2017 "Courageous Campers"</div>
        <div class="program__dates">June 19 - August 18</div>
      </div>
      <p class="program__body">Mon-Fri 8 am to 4 pm. <b>Open to all kids entering grades 1 to 8.</b><br>Day camp is chock full of activities like swimming, rock wall, archery, zipline, sports, campfires and much more!<br>Daily lunch and snack included.<br>Before and after-care available at an extra rate.</p>
      <div class="program__price">$130 per week</div>
    </div>
    <div class="program">
      <div class="program__head">
        <div class="program__title">Overnight Camp 2017</div>
        <div class="program__dates">July 16 - 22</div>
      </div>
      <p class="program__body"><b>Open to all kids ages 8 to 14.</b><br>Spend the week making new friends, sleeping in cabins, climbing the rock wall and ziplining under the stars!<br>Our special guest speaker will lead twice daily chapel sessions that will challenge campers to grow in their faith.</p>
      <div class="program__price">$325</div>
    </div>
  </div>

  <p class="promo">Register and pay for 7 weeks by May 1st,<strong>get 2 FREE!</strong></p>

  <div class="phone">603-555-0148</div>

  <p class="footer"><b>Website:</b> www.maplebrook-example.org <b>Address:</b> 41 Cedar Vale Rd. Lisford, NH 03999</p>
</section>

<section class="card card--back">
  <div class="brand"><span class="brand__dot"></span><div class="brand__name"><span>Camp</span><span>Maplebrook</span></div></div>
  <div class="back__label">Address:</div>
  <div class="back__address">41 Cedar Vale Rd. Lisford, NH 03999</div>
  <div class="back__divider"></div>
  <div class="back__stamp"></div>
</section>

</body>
</html>
```